Summit Shield Coatings Inc facebook rebranding

We had our facebook design done 3 years ago and we need to get it more updated and attractive. I have attached what we already use and here below is a link to our page. i have 2 locations so when we pick a design we will need files to have each locations logo and phone number
location 1- Summit Shield Coatings Inc. 469-555-0148
Location 2- Summit Shield Coatings of west texas inc. 806-555-0192
here is link
Target Market(s)
contractors and homeowners
Industry/Entity Type
Insulation
Font styles to use
Serif
Colors
0054AA
0677BA
7BADD7
CADEEF
E8F1F8

```html
<!DOCTYPE html>
<html lang="en">
<head>
<meta charset="utf-8">
<title>Summit Shield Coatings – Facebook Post</title>
<link rel="stylesheet" href="https://fonts.googleapis.com/css2?family=Playfair+Display:ital,wght@0,700;0,800;1,600&family=Source+Serif+4:wght@500;600;700&display=swap">
<style>
  :root {
    --deep: #003a78;
    --royal: #0054aa;
    --sky: #0677ba;
    --soft: #7badd7;
    --pale: #cadeef;
    --mist: #e8f1f8;
    --white: #ffffff;
  }
  html, body { margin: 0; padding: 0; overflow: hidden; background: #ffffff; }
  .post {
    position: relative;
    width: 1200px;
    height: 1200px;
    overflow: hidden;
    font-family: "Source Serif 4", serif;
  }
  .backdrop { position: absolute; inset: 0; }
  .brand {
    position: absolute;
    left: 30px; top: 148px;
    width: 420px;
    text-align: center;
    margin: 0;
    font-family: "Playfair Display", serif;
    font-weight: 800;
    font-size: 35px;
    line-height: 1.2;
    color: var(--deep);
  }
  .headline {
    position: absolute;
    left: 44px; top: 382px;
    margin: 0;
    font-family: "Playfair Display", serif;
  }
  .headline .strong {
    display: block;
    font-weight: 800;
    font-size: 50px;
    line-height: 70px;
    color: var(--pale);
  }
  .headline .light {
    display: block;
    font-style: italic;
    font-weight: 600;
    font-size: 54px;
    line-height: 72px;
    color: var(--white);
  }
  .rule { position: absolute; left: 44px; top: 546px; }
  .services-title {
    position: absolute;
    left: 57px; top: 594px;
    margin: 0;
    font-family: "Playfair Display", serif;
    font-weight: 700;
    font-size: 32px;
    color: var(--soft);
  }
  .services-title .arrow { font-size: 24px; margin-right: 14px; }
  .services-list {
    position: absolute;
    left: 72px; top: 650px;
    margin: 0; padding: 0 0 0 17px;
    list-style: none;
    border-left: 1.5px solid var(--soft);
  }
  .services-list li {
    position: relative;
    font-weight: 500;
    font-size: 25px;
    line-height: 39px;
    color: var(--mist);
  }
  .services-list li::before {
    content: "";
    position: absolute;
    left: -22px; top: 17px;
    width: 7px; height: 7px;
    border-radius: 50%;
    background: var(--white);
  }
  .phone {
    position: absolute;
    display: flex;
    align-items: center;
    height: 52px;
    border-radius: 26px;
    box-shadow: 0 3px 6px rgba(0, 40, 90, 0.25);
  }
  .phone .icon {
    width: 56px; height: 52px;
    display: flex; align-items: center; justify-content: center;
  }
  .phone .number {
    flex: 1;
    height: 52px;
    border-radius: 26px;
    background: var(--sky);
    color: var(--white);
    font-weight: 700;
    font-size: 29px;
    display: flex; align-items: center; justify-content: center;
  }
  .phone-west { left: 69px; top: 926px; width: 326px; background: var(--royal); }
  .phone-lubbock { left: 791px; top: 1018px; width: 326px; background: var(--white); }
  .address {
    position: absolute;
    margin: 0;
    font-style: normal;
    font-weight: 600;
    font-size: 24px;
    line-height: 32px;
  }
  .address-west { left: 101px; top: 1002px; color: var(--royal); }
  .address-lubbock { right: 121px; top: 1097px; color: var(--white); text-align: right; }
  .pin { position: absolute; }
  .available {
    position: absolute;
    left: 98px; top: 1096px;
    margin: 0;
    font-weight: 600;
    font-size: 18px;
    color: var(--deep);
    text-decoration: underline;
  }
  .socials {
    position: absolute;
    left: 89px; top: 1137px;
    display: flex; gap: 11px;
  }
  .socials span {
    width: 32px; height: 32px;
    border-radius: 50%;
    background: var(--royal);
  }
</style>
</head>
<body>
<main class="post">
  <svg class="backdrop" width="1200" height="1200" viewBox="0 0 1200 1200">
    <defs>
      <linearGradient id="paneLight" x1="0" y1="0" x2="1" y2="1">
        <stop offset="0" stop-color="#e8f1f8"/>
        <stop offset="0.6" stop-color="#f4f8fc"/>
        <stop offset="1" stop-color="#cadeef"/>
      </linearGradient>
      <linearGradient id="paneBlue" x1="0" y1="0" x2="0.6" y2="1">
        <stop offset="0" stop-color="#003a78"/>
        <stop offset="0.5" stop-color="#0054aa"/>
        <stop offset="1" stop-color="#0677ba"/>
      </linearGradient>
      <linearGradient id="band" x1="0" y1="0" x2="1" y2="1">
        <stop offset="0" stop-color="#003a78"/>
        <stop offset="1" stop-color="#0054aa"/>
      </linearGradient>
      <radialGradient id="foamTones" cx="0.6" cy="0.45" r="0.7">
        <stop offset="0" stop-color="#f1eeea"/>
        <stop offset="0.6" stop-color="#e2dbd2"/>
        <stop offset="1" stop-color="#c9b59d"/>
      </radialGradient>
    </defs>
    <rect width="1200" height="1200" fill="#e8f1f8"/>
    <polygon points="0,0 398,0 757,595 398,1200 0,1200" fill="url(#paneLight)"/>
    <polygon points="449,0 1200,0 1200,1200 449,1200 809,595" fill="url(#paneBlue)"/>
    <rect x="0" y="333" width="600" height="556" fill="url(#band)"/>
    <circle cx="873" cy="572" r="409" fill="#ffffff"/>
    <circle cx="873" cy="572" r="372" fill="url(#foamTones)" role="img" aria-label="Photo of a gloved installer spraying white foam insulation into wooden wall framing"/>
  </svg>

  <h1 class="brand">Summit Shield Coatings<br>of West Texas</h1>

  <h2 class="headline">
    <span class="strong">PERFORMANCE</span>
    <span class="light">that matters</span>
  </h2>
  <svg class="rule" width="400" height="4" aria-hidden="true">
    <rect width="192" height="2" fill="var(--soft)"/>
    <rect x="192" width="208" height="2" fill="var(--pale)"/>
  </svg>

  <h3 class="services-title"><span class="arrow">&#10142;</span>Services:</h3>
  <ul class="services-list">
    <li>Spray Foam Insulation</li>
    <li>Fiberglass Insulation</li>
    <li>Air Sealing</li>
    <li>Insulation Removal</li>
    <li>Attic Ventilation</li>
  </ul>

  <div class="phone phone-west">
    <span class="icon">
      <svg width="28" height="28" viewBox="0 0 24 24" fill="none" stroke="#ffffff" stroke-width="2" aria-hidden="true">
        <circle cx="12" cy="12" r="10"/>
        <path d="M8.5 7.5c-.8.8-.8 2.5.8 4.6 1.6 2.2 3.4 3.4 4.6 3.4.6 0 1-.4 1.3-.8l-1.6-1.4-1.1.6c-.8-.4-1.9-1.6-2.3-2.4l.6-1.1-1.3-1.7z" fill="#ffffff" stroke-width="0.8"/>
      </svg>
    </span>
    <span class="number">469-555-0148</span>
  </div>

  <svg class="pin" style="left:70px;top:1010px" width="20" height="26" viewBox="0 0 20 26" aria-hidden="true">
    <path d="M10 1a8.5 8.5 0 0 0-8.5 8.5C1.5 16 10 25 10 25s8.5-9 8.5-15.5A8.5 8.5 0 0 0 10 1z" fill="var(--royal)"/>
    <circle cx="10" cy="9.5" r="3.3" fill="#e8f1f8"/>
  </svg>
  <address class="address address-west">2870 Cedar Hollow Rd<br>Mckinney, TX 75070</address>

  <p class="available">Available on:</p>
  <div class="socials" aria-label="Social channels">
    <span></span><span></span><span></span><span></span>
  </div>

  <div class="phone phone-lubbock">
    <span class="icon">
      <svg width="28" height="28" viewBox="0 0 24 24" fill="none" stroke="#0054aa" stroke-width="2" aria-hidden="true">
        <circle cx="12" cy="12" r="10"/>
        <path d="M8.5 7.5c-.8.8-.8 2.5.8 4.6 1.6 2.2 3.4 3.4 4.6 3.4.6 0 1-.4 1.3-.8l-1.6-1.4-1.1.6c-.8-.4-1.9-1.6-2.3-2.4l.6-1.1-1.3-1.7z" fill="#0054aa" stroke-width="0.8"/>
      </svg>
    </span>
    <span class="number">806-555-0192</span>
  </div>

  <address class="address address-lubbock">4118 Mesa Ridge st, lubbock<br>texas 79424</address>
  <svg class="pin" style="left:1090px;top:1104px" width="20" height="26" viewBox="0 0 20 26" aria-hidden="true">
    <path d="M10 1a8.5 8.5 0 0 0-8.5 8.5C1.5 16 10 25 10 25s8.5-9 8.5-15.5A8.5 8.5 0 0 0 10 1z" fill="#ffffff"/>
    <circle cx="10" cy="9.5" r="3.3" fill="#0677ba"/>
  </svg>
</main>
</body>
</html>
```